small auto electrical company needs new logo and business cards !!!

we are a small auto electrical company (Velmor Autos Ltd) that has been running for 13 years the logo we have was put together by dinosaurs so we are looking at re branding the company starting with business cards and a new logo we fit GPS tracking devices for young drivers through there insurance company also we fit hands free systems and dash cameras also safety locks to fleet vehicles we would like bright eye catching colours day glow and neon and quirky designs for the logo our original logo was baby blue which i have added a picture enclosed we would like double sided but have a space to write notes and prices preferably not white on back same colour throughout many thanks
Reason: Just a chance to finalise any designs we want VA logos or V logos - No vlm's and no dinosaurs lol
Business
Installs@velmorautos.co.uk
07922483617
www.Velmorautos.co.uk
Velmor Autos Ltd - Fleets and Insurance Services
- new logo design !!
- Satellite in logo or something attaining to gps
- maybe a car in the logo
- shouldnt have velmor as vlm it is VeLMOR Autos

```html
<!DOCTYPE html>
<html lang="en">
<head>
<meta charset="utf-8">
<title>Velmor Autos Ltd – Business Card</title>
<link rel="stylesheet" href="https://fonts.googleapis.com/css2?family=Open+Sans:wght@400;600&display=swap">
<style>
  :root {
    --backdrop: #1c1c1c;
    --card: #ffffff;
    --brand-blue: #3bbce9;
    --ink: #2b2b2b;
    --ink-soft: #333333;
    --faint-blue: #e9f6fc;
  }
  * { margin: 0; padding: 0; box-sizing: border-box; }
  html, body {
    width: 1200px; height: 741px; overflow: hidden;
    background: var(--backdrop);
    font-family: "Open Sans", sans-serif;
  }
  .canvas { position: relative; width: 1200px; height: 741px; }

  .card {
    position: absolute; top: 229px;
    width: 494px; height: 282px;
    background: var(--card);
    border-radius: 12px;
    overflow: hidden;
  }
  .card--front { left: 100px; }
  .card--back { left: 606px; }

  .brand-name {
    font-family: "Open Sans", sans-serif;
    font-weight: 600;
    color: var(--brand-blue);
    white-space: nowrap;
    line-height: 1;
  }
  .brand-tagline {
    font-family: "Open Sans", sans-serif;
    font-weight: 400;
    color: var(--ink);
    letter-spacing: 1px;
    white-space: nowrap;
    line-height: 1;
  }

  /* Front */
  .front-mark {
    position: absolute; left: 222px; top: 92px;
    width: 50px; height: 50px; border-radius: 50%;
    background: var(--brand-blue);
  }
  .card--front .brand-name {
    position: absolute; left: 0; right: 0; top: 170px;
    text-align: center; font-size: 25px;
  }
  .card--front .brand-tagline {
    position: absolute; left: 0; right: 0; top: 204px;
    text-align: center; font-size: 13px;
  }

  /* Back */
  .back-decoration {
    position: absolute; left: 373px; top: 162px;
    width: 118px; height: 118px; border-radius: 50%;
    background: var(--faint-blue);
  }
  .card--back .brand-name {
    position: absolute; left: 26px; top: 38px; font-size: 29px;
  }
  .card--back .brand-tagline {
    position: absolute; left: 27px; top: 73px; font-size: 13.5px;
  }
  .holder-name {
    position: absolute; left: 26px; top: 131px;
    font-weight: 600;
    font-size: 17px; color: var(--brand-blue);
  }
  .address {
    position: absolute; left: 26px; top: 165px;
    font-size: 13.5px; line-height: 16.5px; color: var(--ink-soft);
    font-style: normal;
  }
  .contact-list {
    position: absolute; left: 26px; top: 210px;
    list-style: none;
  }
  .contact-list li {
    display: flex; align-items: center; gap: 5px;
    height: 17px; font-size: 13.5px; color: var(--ink-soft);
  }
  .contact-icon {
    width: 14px; height: 14px; border-radius: 2px;
    background: var(--brand-blue);
    flex: none;
  }
</style>
</head>
<body>
<main class="canvas">

  <section class="card card--front" aria-label="Card front">
    <div class="front-mark"></div>
    <div class="brand-name">Velmor Autos Ltd</div>
    <div class="brand-tagline">Fleet &amp; Insurance Service</div>
  </section>

  <section class="card card--back" aria-label="Card back">
    <div class="back-decoration"></div>
    <div class="brand-name">Velmor Autos Ltd</div>
    <div class="brand-tagline">Fleet &amp; Insurance Service</div>
    <div class="holder-name">Owen Marsh</div>
    <address class="address">PO BOX 48 Harrow Lane<br>Kestrel Road, Leeds, UK</address>
    <ul class="contact-list">
      <li>
        <svg class="contact-icon" viewBox="0 0 14 14" aria-hidden="true">
          <path d="M4 3 L5.6 3 L6.2 5.4 L5.2 6.2 Q6 8 7.8 8.8 L8.6 7.8 L11 8.4 L11 10 Q10.5 11 9.5 11 Q3 10.5 3 4.5 Q3 3.5 4 3 Z" fill="#fff"/>
        </svg>
        07700 900461
      </li>
      <li>
        <svg class="contact-icon" viewBox="0 0 14 14" aria-hidden="true">
          <rect x="3" y="4" width="8" height="6" fill="none" stroke="#fff" stroke-width="1"/>
          <path d="M3 4 L7 7.5 L11 4" fill="none" stroke="#fff" stroke-width="1"/>
        </svg>
        Installs@velmorautos.co.uk
      </li>
      <li>
        <svg class="contact-icon" viewBox="0 0 14 14" aria-hidden="true">
          <circle cx="7" cy="7" r="4" fill="none" stroke="#fff" stroke-width="0.9"/>
          <ellipse cx="7" cy="7" rx="1.8" ry="4" fill="none" stroke="#fff" stroke-width="0.8"/>
          <path d="M3 7 H11" stroke="#fff" stroke-width="0.8"/>
        </svg>
        www.Velmorautos.co.uk
      </li>
    </ul>
  </section>

</main>
</body>
</html>
```